Yard Signs - Fiber Optic Customer

I need an awesome design for a yard sign for our new customers.  We are installing a fiber optic network and are going to give new customers the option to put a yard sign up in exchange for a free month of service.  I want to use plankmerle.example.  A blank template is available there for the large (27x18) yard signs.
Requirements:
-our website is (needs to be on sign):  www.dovernetlink.example
-our phone:  555-814-2063
-our logo
-a graphic that conveys 'connected'
I want it to say something to the effect.. I'm connected to Dovern Fiber.  The fastest high-speed internet available.  Crystal clear telephone.  I don't necessarily need that specific wording, something along those lines.
Contact me with questions:  paul@dovernetlink.example

```html
<!DOCTYPE html>
<html lang="en">
<head>
<meta charset="utf-8">
<title>Dovern Fiber Yard Sign</title>
<link rel="stylesheet" href="https://fonts.googleapis.com/css2?family=Open+Sans:wght@400;600;700&family=Fredoka:wght@600;700&family=Archivo+Narrow:wght@700&display=swap">
<style>
  :root {
    --sky-light: #4fd2f0;
    --sky-mid: #1aa7e6;
    --sky-deep: #0c6fd0;
    --navy: #0a3f9a;
    --panel: rgba(20, 110, 185, 0.55);
    --panel-dark: rgba(12, 90, 170, 0.6);
    --white: #ffffff;
    --soft-white: #eaf6ff;
    --yellow: #ffe21a;
    --phone-box: #1d5fc6;
    --sea-top: #2a78d4;
    --sea-bottom: #0c3f8f;
  }
  * { box-sizing: border-box; margin: 0; padding: 0; }
  html, body { width: 1200px; height: 808px; overflow: hidden; background: #ffffff; }
  .sign {
    position: relative;
    width: 1200px;
    height: 808px;
    overflow: hidden;
    background: linear-gradient(160deg, var(--sky-light) 0%, var(--sky-mid) 35%, var(--sky-deep) 75%, var(--navy) 100%);
    font-family: "Open Sans", sans-serif;
  }
  .decor { position: absolute; inset: 0; }
  .sea {
    position: absolute;
    left: 0; top: 670px; width: 1200px; height: 138px;
    background: linear-gradient(180deg, var(--sea-top) 0%, var(--sea-bottom) 100%);
  }
  .laptop-surfer {
    position: absolute;
    left: 24px; top: 486px; width: 360px; height: 300px;
    border-radius: 10px;
    background: linear-gradient(200deg, #8fd9c9 0%, #2f9a7a 45%, #2a3a4a 100%);
  }
  .brand {
    position: absolute;
    left: 80px; top: 62px;
    display: flex; align-items: center; gap: 18px;
  }
  .brand-dot {
    width: 46px; height: 46px; border-radius: 50%;
    background: var(--white);
  }
  .brand-name {
    font-family: "Fredoka", sans-serif;
    font-weight: 700;
    font-size: 104px;
    line-height: 1;
    color: var(--white);
    letter-spacing: 2px;
  }
  .feature {
    position: absolute;
    color: var(--soft-white);
    text-align: center;
    text-transform: uppercase;
  }
  .feature-phone {
    left: 210px; top: 220px; width: 424px; height: 116px;
    background: var(--panel);
    font-size: 34px; line-height: 44px; letter-spacing: 3px;
    padding-top: 14px;
  }
  .feature-internet {
    left: 0; top: 350px; width: 634px; height: 142px;
    background: var(--panel-dark);
    font-size: 37px; line-height: 48px; letter-spacing: 1px;
    padding-top: 20px;
  }
  .feature-internet strong { font-weight: 700; }
  .cta {
    position: absolute;
    left: 500px; top: 492px; width: 460px;
    text-align: center;
    color: var(--white);
    font-family: "Fredoka", sans-serif;
    font-weight: 600;
  }
  .cta-lead { font-size: 58px; line-height: 62px; }
  .cta-name { font-size: 90px; line-height: 86px; font-weight: 700; }
  .web {
    position: absolute;
    left: 456px; top: 638px; width: 560px;
    text-align: center;
    color: var(--yellow);
    font-family: "Archivo Narrow", sans-serif;
    font-weight: 700;
    font-size: 36px;
    line-height: 42px;
  }
  .phone {
    position: absolute;
    left: 546px; top: 686px; width: 396px; height: 64px;
    background: var(--phone-box);
    color: var(--white);
    font-size: 38px; line-height: 64px;
    text-align: center;
    letter-spacing: 1px;
  }
</style>
</head>
<body>
<main class="sign">
  <svg class="decor" width="1200" height="808" viewBox="0 0 1200 808" aria-hidden="true">
    <path d="M520 0 C 560 300, 900 480, 1200 560 L1200 620 C 880 540, 520 360, 470 0 Z" fill="#ffffff" opacity="0.25"/>
    <path d="M640 0 C 650 250, 880 430, 1200 520 L1200 556 C 860 470, 610 290, 600 0 Z" fill="#ffffff"/>
    <path d="M690 0 C 700 220, 900 400, 1200 470 L1200 500 C 880 430, 668 260, 664 0 Z" fill="#1b8fe0"/>
  </svg>

  <svg class="decor" width="1200" height="808" viewBox="0 0 1200 808">
    <defs>
      <clipPath id="photo-circle"><circle cx="1212" cy="-72" r="512"/></clipPath>
      <linearGradient id="photo-tone" x1="0" y1="0" x2="1" y2="1">
        <stop offset="0" stop-color="#e8ecef"/>
        <stop offset="0.5" stop-color="#c9b8ad"/>
        <stop offset="1" stop-color="#8fa3b3"/>
      </linearGradient>
    </defs>
    <circle cx="1212" cy="-72" r="540" fill="#ffffff"/>
    <circle cx="1212" cy="-72" r="524" fill="#2a9ae6"/>
    <g clip-path="url(#photo-circle)">
      <rect x="690" y="0" width="510" height="440" fill="url(#photo-tone)" role="img" aria-label="Photo of a smiling woman holding a mobile phone"/>
    </g>
    <g fill="#2a8ae0">
      <rect x="884" y="186" width="14" height="74"/>
      <rect x="904" y="208" width="14" height="52"/>
      <rect x="924" y="226" width="14" height="34"/>
      <rect x="952" y="186" width="8" height="74"/>
      <path d="M942 164 L970 164 L956 186 Z"/>
    </g>
  </svg>

  <div class="sea" role="img" aria-label="Photo of open blue sea"></div>
  <div class="laptop-surfer" role="img" aria-label="Illustration of a surfer riding a wave out of a laptop screen"></div>

  <div class="brand">
    <span class="brand-dot"></span>
    <span class="brand-name">DOVERN</span>
  </div>

  <p class="feature feature-phone">Crystal&nbsp; Clear<br>Telephone</p>
  <p class="feature feature-internet">The Fastest<br><strong>High-Speed</strong> Internet</p>

  <div class="cta">
    <p class="cta-lead">Connecte to</p>
    <p class="cta-name">DOVERN</p>
  </div>

  <p class="web">WWW.DOVERNETLINK.EXAMPLE</p>
  <p class="phone">555-814-2063</p>
</main>
</body>
</html>
```